Contact card for an aggressive entrepreneur

I am looking for a business/contact card as an individual. I operate under the company name The Varden Collective, LLC (but don't generally use that other than for billing). I have explored a few ideas and am now turning to artplaza to connect with people more creative than me. I am trying to capture a diverse set of passions, which I will summarize with the following keywords (which may or may not be ON the card and are in no particular order):

entrepreneur
shark diver
MBA
visionary
defenseman
marketing guru
hockey coach
teacher
reader
writer
cook
captain
scuba diver
beach bum
Type A
Brightwater
Vermont
New York
Montauk
founder
leader
focused
driven
teammate father

hope that makes some sense!
Updates

Please note the photo is for reference - unless there is a really creative way to use it I do not need a card with a head shot (I am not a model or an actor!)

Project Deadline Extended
Reason: There have been several requests to submit designs so we will close this project this Wednesday and select a design by this Friday. Thank you to all for your great ideas and submissions!

I am reviewing the designs and will select one by end of day tomorrow, Tuesday, EST
Thank you to all who participated!

Target Market(s)

everyone from business contacts to personal acquaintances

Industry/Entity Type

Business

Requirements
Must have
• Must be utterly original, extraordinary and memorable.
How it achieves that is up to you!
Essential contact information that needs to be included:

phone: (555) 374-1926
email: tomas@vardencollective.example
skype: tomas.varden
Nice to have
• A striking visual whether that is a photo or illustration
Some way of conveying the diversity of what I am and what I do
Feel free to use the printing or physical material of the card to make it stand out.
Should not have
• I am not into "logos" but that being said I do not want to limit creativity in any way so feel free to ignore any part of this brief if you disagree with me. No need to use the attached photo of me, but that's what I look like.

```html
<!DOCTYPE html>
<html lang="en">
<head>
<meta charset="utf-8">
<title>Tomas Varden – Contact Card</title>
<link rel="stylesheet" href="https://fonts.googleapis.com/css2?family=Exo:wght@200;300&display=swap">
<style>
  :root {
    --page: #e9e7e3;
    --card: #1b1b1b;
    --keyword: #3a3a3a;
    --rule: #2c2c2c;
    --accent: #1ea9e6;
    --label: #8c8c8c;
  }
  html, body {
    margin: 0;
    width: 1200px;
    height: 900px;
    overflow: hidden;
    background: var(--page);
  }
  .card {
    position: absolute;
    left: 100px;
    top: 164px;
    width: 1000px;
    height: 572px;
    background: var(--card);
    overflow: hidden;
    font-family: "Exo", sans-serif;
    box-shadow: 0 10px 30px rgba(0,0,0,0.25);
  }
  .identity {
    position: absolute;
    left: 80px;
    top: 210px;
  }
  .name {
    margin: 0;
    font-weight: 300;
    font-size: 54px;
    line-height: 1;
    color: var(--accent);
    letter-spacing: 0.03em;
    text-transform: uppercase;
    white-space: nowrap;
  }
  .contact {
    margin: 34px 0 0;
    font-size: 15px;
    line-height: 1.6;
    font-weight: 300;
  }
  .contact__row { display: block; white-space: nowrap; }
  .contact__label { color: var(--label); display: inline-block; width: 56px; }
  .contact__value { color: var(--accent); }

  .divider {
    position: absolute;
    left: 640px;
    top: 80px;
    width: 1px;
    height: 412px;
    background: var(--rule);
  }
  .keywords {
    position: absolute;
    right: 80px;
    top: 86px;
    margin: 0;
    padding: 0;
    list-style: none;
    text-align: right;
    font-weight: 200;
    font-size: 22px;
    line-height: 1;
    letter-spacing: 0.12em;
    text-transform: uppercase;
    color: var(--keyword);
  }
  .keywords__item { margin: 0 0 22px; white-space: nowrap; }
  .keywords__item:last-child { margin-bottom: 0; }
</style>
</head>
<body>
  <article class="card">
    <div class="identity">
      <h1 class="name">Tomas Varden</h1>
      <p class="contact">
        <span class="contact__row"><span class="contact__label">phone:</span><span class="contact__value">(555) 374-1926</span></span>
        <span class="contact__row"><span class="contact__label">email:</span><span class="contact__value">tomas@vardencollective.example</span></span>
        <span class="contact__row"><span class="contact__label">skype:</span><span class="contact__value">tomas.varden</span></span>
      </p>
    </div>

    <div class="divider"></div>

    <ul class="keywords">
      <li class="keywords__item">Shark Diver</li>
      <li class="keywords__item">Hockey Coach</li>
      <li class="keywords__item">Defenseman</li>
      <li class="keywords__item">Teacher</li>
      <li class="keywords__item">Writer</li>
      <li class="keywords__item">Cook</li>
      <li class="keywords__item">Beach Bum</li>
      <li class="keywords__item">Driven</li>
      <li class="keywords__item">Teammate</li>
    </ul>
  </article>
</body>
</html>
```